New Web Design Project

New Roofing Website homepage mockup

Complete design document here: https://files.plenovark.com/document/d/7kRtWmZpQ2vLxB9nHcYdF4sJgTuEaOiMbNwXzCyVqhr/edit?usp=sharing
Updates

PROJECT IS NOW CLOSED. ANY NEW SUBMISSIONS WILL BE AUTO REJECTED

Number of Pages Required

1 page

Font styles to use
Sans Serif

```html
<!DOCTYPE html>
<html lang="en">
<head>
<meta charset="utf-8">
<title>SummitLine Roofing — Built Right, Built to Last</title>
<link href="https://fonts.googleapis.com/css2?family=Poppins:ital,wght@0,300;0,400;0,500;0,600;0,700;1,300&display=swap" rel="stylesheet">
<style>
:root{
  --blue:#29a3dd;
  --navy:#0f2a44;
  --ink:#333;
  --muted:#777;
  --title-gray:#5a5a5a;
  --band:#efefef;
  --dark:#2a2f34;
  --gold-a:#fbd23d;
  --gold-b:#f4a623;
  --white:#fff;
}
*{box-sizing:border-box;margin:0;padding:0}
html,body{width:1200px;height:3615px;overflow:hidden}
body{position:relative;font-family:'Poppins',sans-serif;color:var(--ink);background:var(--white)}
.abs{position:absolute}
.photo{position:absolute}
.btn{position:absolute;display:flex;align-items:center;justify-content:center;border-radius:20px;background:linear-gradient(180deg,var(--gold-a),var(--gold-b));color:#2b2b2b;font-weight:600;font-size:11px;box-shadow:0 3px 8px rgba(244,166,35,.35)}
.section-title{position:absolute;left:0;width:1200px;text-align:center;font-size:22px;font-weight:500;color:var(--title-gray);text-transform:uppercase}
.section-title span{color:var(--blue)}
.section-title::after{content:"";display:block;width:34px;height:2px;background:var(--blue);margin:6px auto 0}

/* header */
.logo-box{left:163px;top:0;width:161px;height:91px;background:#fff;box-shadow:0 4px 12px rgba(0,0,0,.2);border-radius:0 0 6px 6px;display:flex;align-items:center;justify-content:center;gap:6px}
.logo-box .mark{width:12px;height:12px;background:var(--blue)}
.brand{font-weight:600;color:var(--blue);font-size:13px;letter-spacing:.3px;text-transform:uppercase}
.nav{left:324px;top:0;width:713px;height:63px;background:#fff;border-radius:0 0 6px 0;box-shadow:0 4px 12px rgba(0,0,0,.15)}
.nav a{position:absolute;top:24px;font-size:10.5px;letter-spacing:1px;color:#666;text-decoration:none;text-transform:uppercase}
.nav a.active{color:var(--blue)}
.nav a.active::after{content:"";display:block;width:100%;height:1px;background:var(--blue);margin-top:3px}

/* hero */
.hero-photo{left:0;top:0;width:1200px;height:600px;background:linear-gradient(160deg,#4a5058 0%,#3a4047 40%,#2c3238 70%,#3b4a3a 100%)}
.hero-welcome{left:596px;top:265px;width:400px;text-align:center;color:#fff;font-size:21px;font-weight:300;letter-spacing:1px}
.hero-head{left:520px;top:295px;width:552px;text-align:center;color:var(--blue);font-size:58px;font-weight:700;line-height:60px;letter-spacing:3px}

/* services */
.svc-photo{width:428px;height:247px;border-radius:0 0 10px 10px}
.svc-frame{border:1.5px solid rgba(255,255,255,.85);border-radius:10px}
.svc-card{background:#fff;box-shadow:0 2px 10px rgba(0,0,0,.15);padding:14px 15px}
.card-h{font-size:19px;font-weight:400;color:#2b2b2b;text-transform:uppercase}
.card-h::after{content:"";display:block;width:34px;height:2px;background:var(--blue);margin-top:3px}
.card-p{font-size:10.5px;line-height:16px;color:#888;font-weight:300;margin-top:9px}
.bul{display:grid;grid-template-columns:1fr 1fr;gap:4px 10px;margin-top:10px;font-size:11.5px;color:#444;list-style:none}
.bul li::before{content:"◇";font-size:9px;margin-right:5px;color:#333}

/* welcome */
.welcome-text{left:163px;top:1197px;width:488px;font-size:10.5px;line-height:16.8px;color:#7a7a7a;font-weight:300}
.welcome-text p+p{margin-top:10px}
.circle{border-radius:50%}

/* roofs */
.roof-box{left:585px;top:1677px;width:452px;height:223px;background:#fff;box-shadow:0 2px 12px rgba(0,0,0,.15);padding:18px 20px}
.ticks{display:grid;grid-template-columns:136px 108px 100px;gap:6px 0;margin-top:14px;font-size:12px;color:#666;list-style:none}
.ticks li{display:flex;align-items:center;gap:6px}

/* projects */
.proj{width:268px;height:163px;border-radius:3px}
.proj-hover{display:flex;align-items:center;justify-content:center;color:#fff;font-size:16px;letter-spacing:1px;background:rgba(25,30,36,.82)}
.proj-hover::before{content:"";position:absolute;inset:6px;border:2px solid var(--blue);border-radius:2px}

/* estimate */
.est-img{width:206px;height:126px}
.est-card{width:189px;height:171px;background:#fff;box-shadow:0 2px 10px rgba(0,0,0,.15);text-align:center;padding-top:10px}
.est-card .tier{font-size:11.5px;color:#444}
.est-card .name{font-size:17px;font-weight:500;color:#333;margin-top:3px}
.est-card .desc{font-size:10.5px;line-height:14px;color:#999;font-weight:300;margin:4px 18px 0}
.est-card .info{font-size:11.5px;color:var(--blue);margin-top:9px}
.est-card .btn{position:relative;margin:9px auto 0;width:140px;height:26px;font-size:11px}

/* clients */
.clients{left:0;top:2999px;width:1200px;height:275px;background:linear-gradient(180deg,#32373d,#23272b)}
.quote{left:222px;top:3082px;width:756px;text-align:center;font-size:11.5px;line-height:16.6px;font-style:italic;font-weight:300;color:#eee}
.qmark{font-size:30px;color:#777;font-style:normal;vertical-align:-10px;line-height:0}

/* call band */
.call-left{left:0;top:3274px;width:1200px;height:52px;background:#555a60}
.call-text{left:196px;top:3287px;color:#fff;font-size:22px;font-weight:500;letter-spacing:2px}
.call-num{left:709px;top:3277px;color:var(--navy);font-size:34px;font-weight:600;letter-spacing:1px}

/* footer */
.foot-links{left:0;top:3420px;width:1200px;display:flex;justify-content:center;gap:0;font-size:11px;color:#444}
.foot-links span{margin:0 22px}
.foot-col{width:140px;text-align:center;font-size:10.5px;line-height:15px;color:#555}
.pill{left:404px;top:3533px;width:244px;height:28px;border:1px solid #ddd;border-radius:14px;display:flex;align-items:center;justify-content:center;gap:7px;font-size:10.5px;color:#555}
.social{width:27px;height:27px;border-radius:50%;border:1px solid #ccc;background:#fff}
.copy{left:0;top:3583px;width:1200px;border-top:1px solid #e4e4e4;text-align:center;padding-top:7px;font-size:10px;color:#888}
</style>
</head>
<body>

<!-- HERO -->
<div class="photo hero-photo" role="img" aria-label="Two-storey grey shingled house with a freshly roofed gable, trees and driveway at dusk"></div>
<svg class="abs" style="left:0;top:380px" width="1200" height="240" viewBox="0 380 1200 240">
  <path d="M0,398 C300,510 600,600 790,590 C960,580 1100,520 1200,468 L1200,620 L0,620 Z" fill="var(--blue)"/>
  <path d="M0,402 C300,505 560,560 740,566 C920,570 1080,530 1200,500 L1200,620 L0,620 Z" fill="#fff"/>
</svg>

<div class="abs logo-box"><span class="mark"></span><span class="brand">SummitLine Roofing</span></div>
<nav class="abs nav">
  <a class="active" style="left:237px">Home</a>
  <a style="left:290px">About Us</a>
  <a style="left:383px">Services</a>
  <a style="left:473px">Blog</a>
  <a style="left:539px">Reviews</a>
  <a style="left:624px">Contact Us</a>
</nav>

<div class="abs hero-welcome">Welcome to</div>
<h1 class="abs hero-head">BUILT RIGHT,<br>BUILT TO LAST</h1>
<div class="btn" style="left:699px;top:437px;width:192px;height:31px;font-size:11px;letter-spacing:.5px">GET AN INSTANT ESTIMATE</div>

<!-- SERVICES -->
<h2 class="section-title" style="top:614px">Our <span>Services</span></h2>

<div class="photo svc-photo" style="left:163px;top:672px;background:linear-gradient(180deg,#5c6066,#3e4246 60%,#2f3336)" role="img" aria-label="Close view of dark slate roof shingles"></div>
<div class="abs svc-frame" style="left:179px;top:689px;width:395px;height:230px"></div>
<div class="abs svc-card" style="left:184px;top:886px;width:384px;height:176px">
  <h3 class="card-h">Highlight</h3>
  <p class="card-p">Sed ut perspiciatis unde omnis iste natus error sit voluptatem accusantium doloremque laudantium, totam rem aperiam, eaque ipsa quae ab illo inventore veritatis et quasi architecto beatae vitae dicta sunt explicabo.</p>
  <ul class="bul" style="grid-template-columns:134px 1fr"><li>Roof Installation</li><li>Roof Repair</li></ul>
</div>

<div class="photo svc-photo" style="left:609px;top:672px;background:linear-gradient(180deg,#8fb6d8,#c9d2d8 45%,#7b7f84)" role="img" aria-label="White house with rounded turret under roof replacement, ladder against the wall"></div>
<div class="abs svc-frame" style="left:626px;top:689px;width:395px;height:230px"></div>
<div class="abs svc-card" style="left:632px;top:886px;width:383px;height:176px">
  <h3 class="card-h">Additional Services</h3>
  <p class="card-p">Sed ut perspiciatis unde omnis iste natus error sit voluptatem accusantium doloremque laudantium, totam rem aperiam, eaque ipsa quae ab illo inventore veritatis et quasi architecto beatae vitae dicta sunt explicabo.</p>
  <ul class="bul" style="grid-template-columns:162px 1fr"><li>Windows/Skylights</li><li>Gutters</li><li>Siding</li><li>Interior leak damage repairs</li></ul>
</div>

<!-- WELCOME -->
<svg class="abs" style="left:0;top:1100px" width="1200" height="470" viewBox="0 1100 1200 470">
  <path d="M0,1102 L1200,1102 L1200,1455 C1080,1520 960,1555 820,1556 C620,1558 400,1480 210,1418 L0,1418 Z" fill="var(--band)"/>
  <path d="M210,1418 C420,1490 640,1562 830,1560 C980,1558 1100,1510 1200,1454 L1200,1478 C1100,1540 980,1565 830,1563 C620,1560 420,1490 210,1418 Z" fill="var(--blue)"/>
</svg>
<h2 class="section-title" style="top:1137px">Welcome to <span>SummitLine Roofing</span></h2>
<div class="abs welcome-text">
  <p>After over a decade of general contracting we continue to see a repetitive trend by the roof purchase process where home owners are constantly left confused, nervous and worried when they need a new roof. As one of the most important features of keeping your home safe, this is unacceptable. SummitLine Roofing was created to break this trend.</p>
  <p>Our process starts by coming to meet you at your home, learning your needs, and suggesting what we would do if it were our home. We will educate you on suggested materials, installation process, warranty information and available financing. When we both determine we can solve your needs, material selection will be confirmed, and your project will be scheduled at a time that best works for you. The project will then be executed. Once the work is completed, we will speak to you to make sure you are satisfied and the job went as you expected.</p>
</div>
<div class="btn" style="left:451px;top:1389px;width:199px;height:28px">Read More SummitLine Roofing</div>
<div class="photo circle" style="left:676px;top:1202px;width:221px;height:221px;background:linear-gradient(180deg,#b9d3ea,#cfd5d6 50%,#5f7f45)" role="img" aria-label="Colonial-style home with grey roof and green lawn"></div>
<div class="photo circle" style="left:823px;top:1287px;width:190px;height:190px;border:6px solid #fff;background:linear-gradient(180deg,#8fb6d8,#d8dde2 55%,#6e7378)" role="img" aria-label="White house with turret during roof work"></div>

<!-- ROOFS -->
<h2 class="section-title" style="top:1594px">Our <span>Roofs</span></h2>
<div class="photo" style="left:163px;top:1655px;width:469px;height:268px;background:linear-gradient(160deg,#3f5a33,#e4e6e8 40%,#7a7f85 60%,#4b6b38)" role="img" aria-label="Aerial view of a large white farmhouse with dark grey roof and stone terrace"></div>
<div class="abs roof-box">
  <h3 class="card-h">Roofs Types</h3>
  <p class="card-p" style="color:#888">Lorem ipsum dolor sit amet, consectetur adipiscing elit, sed do eiusmod tempor incididunt ut labore et dolore magna aliqua. Ut enim ad minim veniam, quis nostrud exercitation ullamco laboris nisi ut aliquip ex ea commodo consequat.</p>
  <ul class="ticks">
    <li><svg width="11" height="11" viewBox="0 0 11 11"><rect x=".5" y=".5" width="10" height="10" rx="2" fill="none" stroke="#29a3dd"/><path d="M2.5 5.5l2 2 4-4.5" stroke="#29a3dd" fill="none" stroke-width="1.4"/></svg>Cedar</li>
    <li><svg width="11" height="11" viewBox="0 0 11 11"><rect x=".5" y=".5" width="10" height="10" rx="2" fill="none" stroke="#29a3dd"/><path d="M2.5 5.5l2 2 4-4.5" stroke="#29a3dd" fill="none" stroke-width="1.4"/></svg>Metal</li>
    <li><svg width="11" height="11" viewBox="0 0 11 11"><rect x=".5" y=".5" width="10" height="10" rx="2" fill="none" stroke="#29a3dd"/><path d="M2.5 5.5l2 2 4-4.5" stroke="#29a3dd" fill="none" stroke-width="1.4"/></svg>Slate</li>
    <li><svg width="11" height="11" viewBox="0 0 11 11"><rect x=".5" y=".5" width="10" height="10" rx="2" fill="none" stroke="#29a3dd"/><path d="M2.5 5.5l2 2 4-4.5" stroke="#29a3dd" fill="none" stroke-width="1.4"/></svg>Asphalt</li>
    <li><svg width="11" height="11" viewBox="0 0 11 11"><rect x=".5" y=".5" width="10" height="10" rx="2" fill="none" stroke="#29a3dd"/><path d="M2.5 5.5l2 2 4-4.5" stroke="#29a3dd" fill="none" stroke-width="1.4"/></svg>Rubber</li>
  </ul>
</div>

<!-- PROJECTS -->
<svg class="abs" style="left:0;top:1965px" width="1200" height="610" viewBox="0 1965 1200 610">
  <path d="M0,1972 L1200,2012 L1200,2568 L0,2484 Z" fill="var(--band)"/>
</svg>
<h2 class="section-title" style="top:2030px">Our <span>Projects</span></h2>
<div class="photo proj" style="left:174px;top:2088px;background:linear-gradient(160deg,#3e5a32,#8d9298 50%,#4b5e3a)" role="img" aria-label="Grey house with dormers and garage among trees"></div>
<div class="photo proj" style="left:465px;top:2088px;background:linear-gradient(160deg,#6c7e8c,#b8bcc0)" role="img" aria-label="Project house in Maple Ridge"></div>
<div class="abs proj proj-hover" style="left:465px;top:2088px">Maple Ridge, ST</div>
<div class="photo proj" style="left:755px;top:2088px;background:linear-gradient(160deg,#3f5a33,#e4e6e8 45%,#6e747a)" role="img" aria-label="Aerial view of white farmhouse with terrace"></div>
<div class="photo proj" style="left:174px;top:2275px;background:linear-gradient(180deg,#bcd4ea,#c8cbc6 50%,#5d7d44)" role="img" aria-label="Colonial home with lawn"></div>
<div class="photo proj" style="left:465px;top:2275px;background:linear-gradient(180deg,#8fb6d8,#dfe3e6 55%,#767b80)" role="img" aria-label="White house with turret during roofing"></div>
<div class="photo proj" style="left:755px;top:2275px;background:linear-gradient(135deg,#7c6a58,#e6e3de 50%,#a08a72)" role="img" aria-label="Curved eyebrow roof over arched window with cedar shingles"></div>
<div class="btn" style="left:538px;top:2456px;width:124px;height:28px">View More ➞</div>

<!-- ESTIMATE -->
<h2 class="section-title" style="top:2594px">Roofing Instant <span>Estimate Calculator</span></h2>

<div class="photo est-img" style="left:168px;top:2660px;background:linear-gradient(90deg,#f39a6c 0%,#f6a878 45%,#4a3d45 55%,#3b3036)" role="img" aria-label="Scalloped clay shingles in orange and dark tones"></div>
<div class="abs est-card" style="left:177px;top:2786px">
  <div class="tier">Good</div><div class="name">Lorem ipsum dolor</div>
  <div class="desc">Sed ut perspiciatis unde omnis iste natus error sit voluptatem.</div>
  <div class="info">View Info</div><div class="btn">Calculate Your Cost</div>
</div>

<div class="photo est-img" style="left:387px;top:2660px;background:linear-gradient(180deg,#5a3a36,#8d5548 60%,#a4604f)" role="img" aria-label="Red-brown wood shake roofing"></div>
<div class="abs est-card" style="left:396px;top:2786px">
  <div class="tier">Better</div><div class="name">Lorem ipsum dolor</div>
  <div class="desc">Sed ut perspiciatis unde omnis iste natus error sit voluptatem.</div>
  <div class="info">View Info</div><div class="btn">Calculate Your Cost</div>
</div>

<div class="photo est-img" style="left:606px;top:2660px;background:linear-gradient(160deg,#a0533e,#c77a5c 50%,#8a4a38)" role="img" aria-label="Terracotta clay tile roofing"></div>
<div class="abs est-card" style="left:614px;top:2786px">
  <div class="tier">Best</div><div class="name">Lorem ipsum dolor</div>
  <div class="desc">Sed ut perspiciatis unde omnis iste natus error sit voluptatem.</div>
  <div class="info">View Info</div><div class="btn">Calculate Your Cost</div>
</div>

<div class="photo est-img" style="left:824px;top:2660px;background:linear-gradient(180deg,#4a4e53,#65696e 60%,#3e4246)" role="img" aria-label="Grey asphalt shingle roofing"></div>
<div class="abs est-card" style="left:832px;top:2786px">
  <div class="tier">Better</div><div class="name">Lorem ipsum dolor</div>
  <div class="desc">Sed ut perspiciatis unde omnis iste natus error sit voluptatem.</div>
  <div class="info">View Info</div><div class="btn">Calculate Your Cost</div>
</div>

<!-- HAPPY CLIENTS -->
<div class="photo clients" role="img" aria-label="Darkened background photo of a house at night"></div>
<h2 class="section-title" style="top:3028px;color:#fff">Happy <span>Clients</span></h2>
<p class="abs quote"><span class="qmark">“</span> We needed to put a new roof on our house, as well as repair a sagging porch roof. Shingles had been flying off and we had had several leaks. Dale provided a very reasonable estimate - well below some of the other HomePro Directory companies. The work was done very promptly and professionally. A couple of issues that arose were settled to our satisfaction and Dale took full ownership of the situation. It was very clear that customer satisfaction is a priority for this company. I would definitely recommend and hire again. <span class="qmark">”</span></p>
<div class="abs" style="left:0;top:3180px;width:1200px;text-align:center;color:var(--blue);font-size:13px;font-weight:500">Owen</div>
<div class="abs" style="left:0;top:3199px;width:1200px;text-align:center;color:#ddd;font-size:10.5px">Fairhaven, ST</div>
<svg class="abs" style="left:574px;top:3233px" width="52" height="12" viewBox="0 0 52 12">
  <circle cx="7" cy="6" r="4.5" fill="none" stroke="#bbb"/>
  <circle cx="26" cy="6" r="4.5" fill="none" stroke="#29a3dd"/><circle cx="26" cy="6" r="1.8" fill="#29a3dd"/>
  <circle cx="45" cy="6" r="4.5" fill="none" stroke="#bbb"/>
</svg>

<!-- CALL BAND -->
<div class="abs call-left"></div>
<svg class="abs" style="left:586px;top:3274px" width="614" height="52" viewBox="0 0 614 52"><path d="M22,0 L614,0 L614,52 L0,52 Z" fill="var(--blue)"/></svg>
<div class="abs call-text">CALL NOW FOR A FREE QUOTE!</div>
<div class="abs call-num">555-201-7788</div>

<!-- FOOTER -->
<div class="abs" style="left:0;top:3358px;width:1200px;display:flex;justify-content:center;align-items:center;gap:7px"><span style="width:12px;height:12px;background:var(--blue)"></span><span class="brand" style="font-size:15px">SummitLine Roofing</span></div>
<div class="abs foot-links"><span>Home</span><span>About Us</span><span>Services</span><span>Blog</span><span>Reviews</span><span>Contact Us</span></div>

<div class="abs foot-col" style="left:401px;top:3452px">
  <svg width="14" height="18" viewBox="0 0 14 18"><path d="M7 1a5.5 5.5 0 0 0-5.5 5.5C1.5 11 7 17 7 17s5.5-6 5.5-10.5A5.5 5.5 0 0 0 7 1z" fill="none" stroke="#666"/><circle cx="7" cy="6.5" r="2" fill="none" stroke="#666"/></svg>
  <div>48 Birch Ln.<br>Fairhaven ST 01234</div>
</div>
<div class="abs foot-col" style="left:536px;top:3452px">
  <svg width="18" height="18" viewBox="0 0 18 18"><path d="M4 2l3 3-2 2c1 2 3 4 5 5l2-2 3 3-2 3C7 15 3 11 2 4z" fill="none" stroke="#666"/></svg>
  <div>555-201-7788</div>
</div>
<div class="abs foot-col" style="left:658px;top:3452px">
  <svg width="18" height="18" viewBox="0 0 18 18"><rect x="2" y="4" width="14" height="12" fill="none" stroke="#666"/><rect x="5" y="1" width="8" height="5" fill="none" stroke="#666"/><path d="M5 9h2M9 9h2M13 9h1M5 12h2M9 12h2" stroke="#666"/></svg>
  <div>555-201-7788</div>
</div>

<div class="abs pill">
  <svg width="13" height="10" viewBox="0 0 13 10"><rect x=".5" y=".5" width="12" height="9" fill="none" stroke="#666"/><path d="M.5.5l6 5 6-5" fill="none" stroke="#666"/></svg>
  dale@summitlineroofing.example
</div>
<div class="abs social" style="left:657px;top:3533px"></div>
<div class="abs social" style="left:694px;top:3533px"></div>
<div class="abs social" style="left:731px;top:3533px"></div>
<div class="abs social" style="left:768px;top:3533px"></div>

<div class="abs copy">Copyright © companyname, All Rights Reserved</div>

</body>
</html>
```